Business Card Design

My company is a health food catering and delivery business. Our colours are a bright turquiose green/blue, black, white and natural brown based beige. I would like the front of my card (working from the outside in; with a turquoise green boarder -quite thick, with a thin black line separating the turquoise boarder from the beige inside the remaining space of the front of the card with my logo in the centre. This should be all that appears on the front.

On the back I would like all the information displayed above on the beige coloured card, with the blurb in the bright turquoise and my contact information in black please. I would like my business name central - Harvest Lantern Kitchen and immediately below with a right alignment - ...Dine with Delight
Below this should follow all that I have displayed above with a left alignment.

Target Market(s)

Cafes, restaurants, individuals, buying agents & super markets

Industry/Entity Type

Catering

Contact Information for Business Card

BACK OF BUSINESS CARD:
Harvest Lantern Kitchen
...Dine with Delight
Deliciously healthy foods - free from gluten, lactose, cane sugar, trans-fat, GMO corn, soy & rice, no artificial flavours, colours or preservatives.
Prepared fresh from locally sourced ingredients, delivered to your door! For individuals, families, corporate, cafes, restaurants & event catering for Toowoomba & surrounds!

PH: 0491 382 907 // orders@harvestlanternkitchen.example
www.harvestlanternkitchen.example
www.social.example/harvestlanternkitchen

Requirements
Must have
• Please supply a modern, easy to read text that will blend nicely with my logo text.
Nice to have
• I really want my business cards to stand out as these will be the template for brochures, menus and website designers to draw inspiration from!
Should not have
• Please do not use Arial, Tahoma or Times Roman text.

```html
<!DOCTYPE html>
<html lang="en">
<head>
<meta charset="utf-8">
<title>Harvest Lantern Kitchen — Business Card</title>
<link rel="stylesheet" href="https://fonts.googleapis.com/css2?family=Dancing+Script:wght@600&family=Yellowtail&family=Mulish:wght@400;800&family=Open+Sans:wght@400&display=swap">
<style>
  :root {
    --turquoise: #7fd3c9;
    --ink: #111111;
    --beige: #ecdfc1;
    --beige-deep: #dccfae;
    --backdrop: #4a4a4c;
  }
  * { box-sizing: border-box; margin: 0; padding: 0; }
  html, body { width: 1200px; height: 926px; overflow: hidden; }
  body {
    background: var(--backdrop);
    position: relative;
    font-family: "Mulish", sans-serif;
    color: var(--ink);
  }
  .card {
    position: absolute;
    left: 250px;
    width: 700px;
    height: 400px;
    background: var(--turquoise);
    padding: 22px;
  }
  .card--front { top: 42px; }
  .card--back { top: 484px; }
  .card__inner {
    width: 100%;
    height: 100%;
    border: 5px solid var(--ink);
    background: var(--beige);
    position: relative;
    overflow: hidden;
  }

  /* Front */
  .logo {
    position: absolute;
    left: 50%;
    top: 50%;
    transform: translate(-50%, -50%);
    display: flex;
    flex-direction: column;
    align-items: center;
    gap: 10px;
  }
  .logo__artwork {
    width: 230px;
    height: 130px;
    border-radius: 6px;
    background: linear-gradient(180deg, #e4d6b6 0%, #cfc2a2 100%);
  }
  .logo__name {
    font-family: "Mulish", sans-serif;
    font-weight: 800;
    font-size: 26px;
    color: var(--ink);
    letter-spacing: 0.5px;
    white-space: nowrap;
  }

  /* Back */
  .back__head {
    padding: 18px 32px 0;
    text-align: center;
  }
  .back__name {
    font-family: "Yellowtail", "Dancing Script", sans-serif;
    font-weight: 400;
    font-size: 50px;
    line-height: 1.05;
    color: var(--ink);
    white-space: nowrap;
  }
  .back__tagline {
    text-align: right;
    font-family: "Open Sans", sans-serif;
    font-size: 13px;
    letter-spacing: 0.5px;
    text-transform: uppercase;
    margin: 0 96px 0 0;
  }
  .back__blurb {
    padding: 8px 22px 0;
    font-weight: 800;
    font-size: 15.5px;
    line-height: 1.32;
    text-align: justify;
  }
  .back__contact {
    position: absolute;
    left: 0; right: 0; bottom: 0;
    height: 92px;
    background: var(--beige-deep);
    padding: 16px 24px;
    display: flex;
    justify-content: space-between;
    font-family: "Open Sans", sans-serif;
    font-size: 13px;
    line-height: 1.6;
    white-space: nowrap;
  }
  .back__contact-col--web { align-self: flex-end; }
  .back__label { font-weight: 400; margin-right: 4px; }
</style>
</head>
<body>
  <section class="card card--front" aria-label="Card front">
    <div class="card__inner">
      <div class="logo">
        <div class="logo__artwork" role="img" aria-label="Logo illustration: a retro chef holding a whisk and a frying pan"></div>
        <div class="logo__name">Harvest Lantern Kitchen</div>
      </div>
    </div>
  </section>

  <section class="card card--back" aria-label="Card back">
    <div class="card__inner">
      <header class="back__head">
        <h1 class="back__name">Harvest Lantern Kitchen</h1>
        <p class="back__tagline">Dine with Delight</p>
      </header>
      <p class="back__blurb">Deliciously healthy foods - free from gluten, lactose, cane sugar, trans-fat, GMO corn, soy &amp; rice, no artificial flavours, colours or preservatives. Prepared fresh from locally sourced ingredients, delivered to your door! For individuals, families, corporate, cafes, restaurants &amp; event catering for Toowoomba &amp; surrounds!</p>
      <footer class="back__contact">
        <div class="back__contact-col">
          <div><span class="back__label">P:</span>0491 382 907</div>
          <div><span class="back__label">E:</span>orders@harvestlanternkitchen.example</div>
        </div>
        <div class="back__contact-col back__contact-col--web">
          <div><span class="back__label">W:</span>harvestlanternkitchen.example</div>
          <div><span class="back__label">F:</span>social.example/harvestlanternkitchen</div>
        </div>
      </footer>
    </div>
  </section>
</body>
</html>
```